Business Card Design Project

We need a double-sided business card design for our e-commerce company. Be as creative as you can.

Reason: Change of logo

Target Market(s)

Business owners

Industry/Entity Type

E-Commerce

Requirements
Must have
• Name (editable)
Mobile number -editable
www.velbiro.com - MUST STAND OUT ALONE
Office address:
27 Marlow Street
#09-04 Westbrook Tower
Singapore 048216

```html
<!DOCTYPE html>
<html lang="en">
<head>
<meta charset="utf-8">
<title>Velbiro business card</title>
<link rel="stylesheet" href="https://fonts.googleapis.com/css2?family=Cabin:wght@400;500;600&display=swap">
<style>
  :root {
    --stage: #2a2a2c;
    --card: #0e1119;
    --accent: #e8632a;
    --accent-deep: #c9451e;
    --text-light: #e6e6e6;
    --mark-faint: #2a1712;
  }
  * { box-sizing: border-box; margin: 0; padding: 0; }
  html, body { width: 1200px; height: 900px; overflow: hidden; }
  body {
    background: var(--stage);
    font-family: "Cabin", "Gill Sans", sans-serif;
    position: relative;
  }
  .card {
    position: absolute;
    left: 250px;
    width: 700px;
    height: 400px;
    background: var(--card);
    border-radius: 26px;
    overflow: hidden;
    box-shadow: 0 10px 30px rgba(0,0,0,.45);
  }
  .card--front { top: 30px; }
  .card--back { top: 470px; border-bottom: 14px solid var(--accent-deep); }

  .brand-name {
    color: var(--accent);
    font-weight: 600;
    letter-spacing: 1px;
  }
  .card--front .brand-name {
    position: absolute;
    left: 0; right: 0; top: 140px;
    text-align: center;
    font-size: 110px;
    line-height: 1;
  }
  .card--back .brand-name {
    position: absolute;
    left: 50px; top: 42px;
    font-size: 58px;
    line-height: 1;
  }
  .contact {
    position: absolute;
    left: 50px; top: 150px;
    color: var(--text-light);
  }
  .contact__name {
    color: var(--accent);
    font-size: 27px;
    font-weight: 400;
    letter-spacing: .5px;
  }
  .contact__role { font-size: 17px; margin-top: 2px; }
  .contact__details {
    margin-top: 26px;
    font-size: 20px;
    line-height: 1.3;
    font-style: normal;
  }
  .label { color: var(--accent); }
  .decor-mark {
    position: absolute;
    right: 60px; top: 30px;
  }
  .website {
    position: absolute;
    right: 40px; bottom: 26px;
    color: var(--accent);
    font-size: 22px;
    letter-spacing: 1px;
  }
</style>
</head>
<body>
  <section class="card card--front" aria-label="Card front">
    <div class="brand-name">velbiro</div>
  </section>

  <section class="card card--back" aria-label="Card back">
    <div class="brand-name">velbiro</div>
    <svg class="decor-mark" width="260" height="260" viewBox="0 0 260 260" aria-hidden="true">
      <circle cx="130" cy="130" r="120" fill="var(--mark-faint)"/>
    </svg>
    <div class="contact">
      <h1 class="contact__name">Daniel Harrow</h1>
      <p class="contact__role">managing director</p>
      <address class="contact__details">
        <span class="label">Mobile</span> 8123 456 789<br>
        <span class="label">Address:</span> 27 Marlow Street<br>
        #09-04 Westbrook Tower<br>
        Singapore 048216
      </address>
    </div>
    <div class="website">www.velbiro.com</div>
  </section>
</body>
</html>
```